PREMIUM AGENCY High End Business Card - A+++ Designers Wanted

** DO NOT ATTEMPT TO CONTACT ME THROUGH SEARCHING ON ZINTREL OR EMAILING ME THROUGH MY WEBSITE **

I need a fresh, contemporary business card designed using the logo attached (BRONSALK)

I have attached the font for BRONSALK

It must have a premium look and feel. The business card size must be STANDARD size.

You can submit either/both VERTICAL or HORIZONTAL designs.

FRONT: It must have the following sample information on

Paul Ardley
Director Operations
Mobile +61 452 118 906
Email paulardley@bronsalk.com
www.bronsalk.com

The REAR of the business card must have the words

CREATE INSPIRE TOMORROW

as part of the design, in the same font (NEXA) attached.

The words do not need to be in capitals, or on the same line, please design this as you see it best working.

ADDITIONAL INFORMATION
======================

The BRONSALK logo must be on the front of the card

I want Ultraviolet printing on the final design, to enhance either the NAME of the person OR the BRONSALK logo OR the words on the back of the card.

Target Market(s)

Agency, Advertising Agency, Creative, Designers

Industry/Entity Type

Media

Contact Information for Business Card

Design Agency, Contemporary, Premium look and feel, High Quality

Font styles to use
Serif
Sans Serif
Other font styles liked:
• ATTACHED TO PROJECT

Requirements
Must have
• BLACK & WHITE as the primary design, and if you feel there can be a highlighted colour, then this can be used.
• The Logo ICON attached is blue, this colour must not be changed.
• I have attached the partner brand BRONSALK MEDIA incase you need to manipulate the original files.
• ** DO NOT ATTEMPT TO CONTACT ME THROUGH SEARCHING ON ZINTREL OR EMAILING ME THROUGH MY WEBSITE **
Nice to have
• Must be Premium. I have attached some sample designs, that I like that would be a good inspiration for where this can be taken.
• My favourite design is is the KESTRAVUE2-BUSINESSCARD-TEMPLATE
Should not have
• No funny or silly standard / off the shelf designs

```html
<!DOCTYPE html>
<html lang="en">
<head>
<meta charset="utf-8">
<title>Bronsalk Business Card</title>
<link rel="stylesheet" href="https://fonts.googleapis.com/css2?family=Montserrat:wght@500;600;700&display=swap">
<style>
  :root {
    --backdrop: #e8e5e0;
    --front-top: #c4c4c4;
    --front-bottom: #949494;
    --ink-dark: #333333;
    --ink-mid: #4f4f4f;
    --band-light: #5a5a5a;
    --band-dark: #333333;
    --rear-centre: #ffffff;
    --rear-edge: #dedede;
    --wordmark: #111111;
    --brand-blue: #27a8e3;
  }
  * { margin: 0; padding: 0; box-sizing: border-box; }
  html, body {
    width: 1200px;
    height: 1000px;
    overflow: hidden;
    background: var(--backdrop);
    font-family: "Montserrat", sans-serif;
  }
  .canvas { position: relative; width: 1200px; height: 1000px; }

  .card {
    position: absolute;
    top: 68px;
    width: 505px;
    height: 864px;
    overflow: hidden;
    box-shadow: 0 4px 14px rgba(0,0,0,0.18);
  }

  /* Front */
  .card-front {
    left: 80px;
    background: linear-gradient(180deg, var(--front-top) 0%, var(--front-bottom) 100%);
  }
  .person-name {
    position: absolute;
    left: 44px;
    top: 52px;
    color: var(--ink-dark);
    font-weight: 600;
    line-height: 1;
  }
  .person-name .first {
    display: block;
    font-size: 154px;
    letter-spacing: -2px;
  }
  .person-name .last {
    display: block;
    font-size: 92px;
    margin-top: 6px;
    letter-spacing: -1px;
  }
  .person-role {
    position: absolute;
    left: 46px;
    top: 294px;
    font-size: 22px;
    font-weight: 500;
    letter-spacing: 1px;
    color: var(--ink-mid);
  }
  .contact-list {
    position: absolute;
    left: 46px;
    top: 664px;
    list-style: none;
  }
  .contact-list li {
    display: flex;
    align-items: center;
    height: 29px;
    font-size: 19px;
    font-weight: 500;
    color: var(--ink-dark);
  }
  .contact-list svg { width: 20px; height: 20px; margin-right: 13px; flex: none; }
  .band-light {
    position: absolute;
    left: 0; bottom: 0;
    width: 100%; height: 26px;
    background: var(--band-light);
  }
  .band-dark {
    position: absolute;
    right: 0; bottom: 0;
    width: 250px; height: 35px;
    background: var(--band-dark);
    clip-path: polygon(22px 0, 100% 0, 100% 100%, 0 100%);
  }

  /* Rear */
  .card-rear {
    left: 621px;
    width: 502px;
    background: radial-gradient(ellipse 60% 50% at 50% 52%, var(--rear-centre) 0%, var(--rear-centre) 35%, var(--rear-edge) 100%);
  }
  .brand-dot {
    position: absolute;
    left: 216px;
    top: 340px;
    width: 70px;
    height: 70px;
    border-radius: 50%;
    background: var(--brand-blue);
  }
  .brand-name {
    position: absolute;
    left: 0; right: 0;
    top: 490px;
    text-align: center;
    font-size: 52px;
    font-weight: 700;
    letter-spacing: 4px;
    color: var(--wordmark);
  }
</style>
</head>
<body>
<main class="canvas">
  <section class="card card-front" aria-label="Card front">
    <h1 class="person-name"><span class="first">PAUL</span><span class="last">ARDLEY</span></h1>
    <p class="person-role">DIRECTOR OPERATIONS</p>
    <ul class="contact-list">
      <li>
        <svg viewBox="0 0 20 20" aria-hidden="true"><rect x="5" y="2" width="10" height="16" rx="1.5" fill="none" stroke="#333" stroke-width="1.8"/><line x1="8" y1="15" x2="12" y2="15" stroke="#333" stroke-width="1.5"/></svg>
        +61 452 118 906
      </li>
      <li>
        <svg viewBox="0 0 20 20" aria-hidden="true"><rect x="2" y="4" width="16" height="12" fill="#333"/><path d="M2 4 L10 11 L18 4 M2 16 L8 10 M18 16 L12 10" fill="none" stroke="#bbb" stroke-width="1.2"/></svg>
        PAULARDLEY@BRONSALK.COM
      </li>
      <li>
        <svg viewBox="0 0 20 20" aria-hidden="true"><rect x="2" y="3" width="16" height="11" fill="none" stroke="#333" stroke-width="1.8"/><rect x="8" y="14" width="4" height="3" fill="#333"/><rect x="5" y="17" width="10" height="1.6" fill="#333"/></svg>
        WWW.BRONSALK.COM
      </li>
    </ul>
    <div class="band-light"></div>
    <div class="band-dark"></div>
  </section>

  <section class="card card-rear" aria-label="Card back">
    <div class="brand-dot"></div>
    <p class="brand-name">BRONSALK</p>
  </section>
</main>
</body>
</html>
```